Criminal Defense Law Firm needs Stationary design Theme for a Business Card, Envelope, and Letterhea

Our Law Firm is seeking a general design concept for a business card, letterhead, and Envelope.

Our website is WillowcrestTrialDesk.com

A design for these three items is requested to keep branding in place for the firm. Would like to keep the Firm Colors on the website consistent with our branding on business cards, letterheads, and mailing envelopes #10 size to be exact.

We would like business cards printed front and back with Law firm Colors from website.

Letterhead with law firm colors as well. Design is not limited to just the header, but the footer can be utilized as well for email, website, phone, fax, etc.

Simple #10 envelope consisting of the same design principles set out in the previous two designs.

```html
<!DOCTYPE html>
<html lang="en">
<head>
<meta charset="utf-8">
<title>Willowcrest Trial Desk Stationery</title>
<link href="https://fonts.googleapis.com/css2?family=Crimson+Text:wght@400;600;700&family=Tinos:wght@400;700&display=swap" rel="stylesheet">
<style>
:root{
  --bg:#d5e7ee;
  --ink:#0d0e10;
  --teal:#1ab3c9;
  --teal-dark:#0f98ad;
  --paper:#ffffff;
  --grey:#e3e3e4;
  --faint:#d9d9d9;
  --text:#1d1d1d;
}
*{margin:0;padding:0;box-sizing:border-box}
html,body{width:1200px;height:1000px;overflow:hidden}
body{background:var(--bg);position:relative;font-family:"Tinos",serif;color:var(--text)}
.brand{display:flex;align-items:center;gap:10px;position:absolute;color:#fff;font-family:"Crimson Text",serif;font-weight:400;letter-spacing:.06em;line-height:1.05}
.brand-dot{border:2px solid #fff;border-radius:50%;flex:none}
.swoosh{position:absolute;left:0;top:0;width:100%}
.watermark{position:absolute;border:6px solid var(--faint);border-radius:50%;opacity:.7}

/* Letterhead */
.letterhead{position:absolute;left:413px;top:100px;width:558px;height:790px;background:var(--paper)}
.letterhead .swoosh{height:135px}
.letterhead .brand{left:22px;top:28px;font-size:17px}
.letterhead .brand-dot{width:38px;height:38px}
.letterhead .watermark{left:185px;top:262px;width:170px;height:170px}
.letter{position:absolute;left:65px;top:180px;width:470px;font-size:10.5px;line-height:14px}
.recipient{margin-bottom:14px}
.letter p{text-align:justify;margin-bottom:12px}
.signature{width:60px;height:26px;margin:6px 0 4px;background:linear-gradient(90deg,#f4f4f4,#ececec)}
.letter-footer{position:absolute;left:0;bottom:0;width:100%;height:70px;background:var(--ink);border-top:7px solid var(--teal);color:#fff;font-size:9.5px;line-height:14px;padding:7px 22px 0}
.letter-footer .left{float:left}
.letter-footer .right{float:right;text-align:right}

/* Envelope */
.envelope{position:absolute;left:68px;top:392px;width:642px;height:278px;background:var(--paper)}
.envelope .swoosh{height:112px}
.envelope .brand{left:16px;top:18px;font-size:17px}
.envelope .brand-dot{width:38px;height:38px}
.envelope .window{position:absolute;left:69px;top:147px;width:194px;height:78px;background:var(--grey);border-radius:12px}
.envelope .watermark{left:440px;top:120px;width:150px;height:150px}
.return-address{position:absolute;right:10px;bottom:6px;text-align:right;color:var(--teal);font-family:"Crimson Text",serif;font-weight:700;font-size:12.5px;line-height:16px}

/* Cards */
.card{position:absolute;left:866px;width:238px;height:133px;border-radius:14px;overflow:hidden}
.card-front{top:240px;background:radial-gradient(ellipse at 60% 40%,#4a4b4f,#1c1d20 75%)}
.card-front .swoosh{height:60px}
.card-front .brand{left:10px;top:10px;font-size:8.5px;gap:5px}
.card-front .brand-dot{width:20px;height:20px;border-width:1.5px}
.holder{position:absolute;left:8px;top:72px;width:88px;text-align:right;font-family:"Crimson Text",serif}
.holder .name{color:var(--teal);font-weight:700;font-size:8.5px;letter-spacing:.04em}
.holder .role{color:#fff;font-size:6.5px}
.divider{position:absolute;left:101px;top:54px;width:1px;height:52px;background:#8d8e92}
.contacts{position:absolute;left:107px;top:56px;list-style:none;color:var(--teal);font-size:6.5px;line-height:8.5px}
.contacts li{display:flex;gap:4px;margin-bottom:2px}
.contacts svg{width:8px;height:8px;flex:none;margin-top:1px}
.card-site{position:absolute;right:0;left:0;bottom:10px;text-align:center;color:#fff;font-size:6.5px;letter-spacing:.05em}
.card-back{top:398px;background:linear-gradient(160deg,#7fd5e1,var(--teal) 55%,var(--teal-dark))}
.card-back .swoosh{height:44px}
.tagline{position:absolute;right:12px;top:9px;text-align:right;color:#fff;font-family:"Crimson Text",serif;font-weight:700;font-size:8.5px;line-height:10px}
.practice{position:absolute;left:0;right:0;top:48px;color:var(--ink);font-size:6.5px;line-height:8.5px}
.practice h3{text-align:center;font-family:"Crimson Text",serif;font-weight:700;font-size:8.5px;margin-bottom:1px;padding-left:0}
.practice-cols{display:flex;justify-content:center;gap:5px}
.practice-cols ul{list-style:none}
.practice-cols ul:first-child{text-align:right;width:106px}
.practice-cols ul:last-child{width:110px}
</style>
</head>
<body>

<section class="letterhead" aria-label="Letterhead">
  <svg class="swoosh" viewBox="0 0 558 135" preserveAspectRatio="none" aria-hidden="true">
    <path d="M0 0H558V72C400 76 200 92 0 122Z" fill="#0d0e10"/>
    <path d="M0 122C200 92 400 76 558 72V84C400 86 200 102 0 136Z" fill="#1ab3c9"/>
  </svg>
  <div class="brand"><span class="brand-dot"></span><span>WILLOWCREST<br>TRIAL DESK</span></div>
  <div class="watermark" aria-hidden="true"></div>
  <div class="letter">
    <div class="recipient">Mr. T. Harwood,<br>22 Alder Row,<br>Kelsworth,<br>Northbridgeshire,<br>KW4 2PL,<br>England, UK</div>
    <p>Dear Mr. Harwood,</p>
    <p>Thank you for meeting with our office last week. We have reviewed the documents you provided and prepared a summary of the next steps in your matter. Please read the enclosed notes carefully and keep them with your records.</p>
    <p>Our team will contact the court clerk this week to confirm the hearing date. If anything changes, we will call you at once. Until then, please do not discuss the case with anyone outside this office, and forward any letters you receive to us without delay.</p>
    <p>We will also gather witness statements and review the arrest report line by line. Any gaps we find will be raised with the prosecutor before the hearing, so that you are well prepared for each stage ahead.</p>
    <p>Should you have any questions, please call our office during business hours. We are glad to help.</p>
    <div>Sincerely,</div>
    <div class="signature" role="img" aria-label="Handwritten signature"></div>
    <div>Your name</div>
  </div>
  <footer class="letter-footer">
    <div class="left">418 Harrow Lane NW,<br>Brookhaven,<br>NM 87190</div>
    <div class="right">505.555.0147<br>info@willowcresttrialdesk.com<br>www.WillowcrestTrialDesk.com</div>
  </footer>
</section>

<section class="envelope" aria-label="Envelope">
  <svg class="swoosh" viewBox="0 0 642 112" preserveAspectRatio="none" aria-hidden="true">
    <path d="M0 0H642V56C450 58 220 72 0 94Z" fill="#0d0e10"/>
    <path d="M0 94C220 72 450 58 642 56V70C450 68 220 84 0 110Z" fill="#1ab3c9"/>
  </svg>
  <div class="brand"><span class="brand-dot"></span><span>WILLOWCREST<br>TRIAL DESK</span></div>
  <div class="window"></div>
  <div class="watermark" aria-hidden="true"></div>
  <address class="return-address">418 Harrow Lane NW,<br>Brookhaven,<br>NM 87190</address>
</section>

<section class="card card-front" aria-label="Business card front">
  <svg class="swoosh" viewBox="0 0 238 60" preserveAspectRatio="none" aria-hidden="true">
    <path d="M0 52C80 38 160 30 238 30V35C160 35 80 44 0 58Z" fill="#ffffff"/>
    <path d="M0 58C80 44 160 35 238 35V40C160 40 80 50 0 62Z" fill="#1ab3c9"/>
  </svg>
  <div class="brand"><span class="brand-dot"></span><span>WILLOWCREST<br>TRIAL DESK</span></div>
  <div class="holder"><div class="name">DANA ORLOV</div><div class="role">attorney-at-law</div></div>
  <div class="divider"></div>
  <ul class="contacts">
    <li><svg viewBox="0 0 8 8"><circle cx="4" cy="4" r="4" fill="#fff"/><path d="M4 1.6a1.5 1.5 0 0 1 1.5 1.5C5.5 4.3 4 6.4 4 6.4S2.5 4.3 2.5 3.1A1.5 1.5 0 0 1 4 1.6z" fill="#1c1d20"/></svg><span>418 Harrow Lane NW<br>Brookhaven, NM 87190</span></li>
    <li><svg viewBox="0 0 8 8"><circle cx="4" cy="4" r="4" fill="#fff"/><path d="M2.6 2h1l.4 1-.6.5a3 3 0 0 0 1.1 1.1l.5-.6 1 .4v1C5 5.8 2.2 5 2.2 2.4z" fill="#1c1d20"/></svg><span>505.555.0147</span></li>
    <li><svg viewBox="0 0 8 8"><circle cx="4" cy="4" r="4" fill="#fff"/><rect x="2" y="2.8" width="4" height="2.6" fill="#1c1d20"/><path d="M2 2.8 4 4.3 6 2.8" stroke="#fff" stroke-width=".5" fill="none"/></svg><span>dana@willowcresttrialdesk.com</span></li>
  </ul>
  <div class="card-site">www.WillowcrestTrialDesk.com</div>
</section>

<section class="card card-back" aria-label="Business card back">
  <svg class="swoosh" viewBox="0 0 238 44" preserveAspectRatio="none" aria-hidden="true">
    <path d="M0 28C80 24 160 28 238 38V44C160 34 80 30 0 34Z" fill="#0d0e10"/>
    <path d="M0 34C80 30 160 34 238 44H0Z" fill="#ffffff" opacity=".25"/>
  </svg>
  <div class="tagline">CLEARING YOUR NAME<br>IS OUR #1 PRIORITY</div>
  <div class="practice">
    <h3>Our Practice Areas</h3>
    <div class="practice-cols">
      <ul><li>Larceny</li><li>DUI/DWI Defense</li><li>Homicide, Attempted Murder</li><li>Domestic Violence</li><li>Assault &amp; Battery</li><li>Drug Crimes</li></ul>
      <ul><li>Minor In Possession</li><li>Probation Violations</li><li>Resisting Arrest, Public Affray</li><li>Robbery, Burglary and Theft</li><li>White Collar Crimes</li><li>Sex Crimes</li></ul>
    </div>
  </div>
</section>

</body>
</html>
```